Freelance business trainer needs a new business card

My business is called Brightpath. I provide training in the workplace on management, coaching and mentoring, and customer service topics for a variety of businesses, colleges and private training providers, and teach on management programs. I need a professional but eye catching business card. Business colours grey and orange. My name Linda Marrowby; Tel 07862 413057; email lmarrowby@brightpath.co.uk; website www.brightpath.co.uk.
Happy to have some sort of logo on front and details on back or all on one side
Target Market(s)
SME businesses and colleges - workshops i run are for adults in the workplace
Industry/Entity Type
Training
Look and feel
Each slider illustrates characteristics of the customer's brand and the style your logo design should communicate.

```html
<!DOCTYPE html>
<html lang="en">
<head>
<meta charset="utf-8">
<title>Brightpath business card</title>
<link rel="stylesheet" href="https://fonts.googleapis.com/css2?family=Open+Sans:wght@400;600;700&display=swap">
<style>
  :root {
    --backdrop: #1c1c1c;
    --card-grey: #434343;
    --brand-orange: #f6921e;
    --paper-white: #ffffff;
    --soft-white: #e9e9e9;
  }
  * { box-sizing: border-box; margin: 0; padding: 0; }
  html, body {
    width: 1200px;
    height: 871px;
    overflow: hidden;
    background: var(--backdrop);
    font-family: "Open Sans", Arial, sans-serif;
  }
  .canvas {
    position: relative;
    width: 1200px;
    height: 871px;
  }
  .card {
    position: absolute;
    left: 270px;
    width: 660px;
    height: 380px;
    background: var(--card-grey);
    overflow: hidden;
    box-shadow: 0 6px 18px rgba(0,0,0,0.45);
  }
  .card--back { top: 36px; }
  .card--front { top: 455px; }

  .brand-name {
    position: absolute;
    color: var(--brand-orange);
    font-weight: 600;
    letter-spacing: 0.5px;
    line-height: 1;
  }
  .card--back .brand-name {
    top: 52px;
    right: 44px;
    font-size: 40px;
  }
  .card--front .brand-name {
    top: 120px;
    left: 64px;
    font-size: 62px;
  }

  .holder {
    position: absolute;
    left: 48px;
    top: 116px;
    color: var(--paper-white);
  }
  .holder__name {
    font-size: 19px;
    font-weight: 700;
  }
  .holder__role {
    font-size: 17px;
    font-weight: 400;
    color: var(--soft-white);
    margin-top: 4px;
    padding-left: 56px;
  }

  .accent-band {
    position: absolute;
    inset: 0;
    width: 660px;
    height: 380px;
  }
  .accent-band .band-white { fill: var(--paper-white); }
  .accent-band .band-orange { fill: var(--brand-orange); }

  .contact-list {
    position: absolute;
    left: 40px;
    top: 268px;
    list-style: none;
    color: var(--paper-white);
    font-size: 18px;
  }
  .contact-list li {
    display: flex;
    align-items: center;
    gap: 12px;
    height: 28px;
  }
  .contact-list svg {
    width: 16px;
    height: 16px;
    fill: var(--card-grey);
    flex: none;
  }

  .website {
    position: absolute;
    left: 64px;
    top: 262px;
    color: var(--paper-white);
    font-size: 22px;
    font-weight: 700;
    letter-spacing: 0.5px;
  }
</style>
</head>
<body>
<main class="canvas">

  <section class="card card--back" aria-label="Card back with contact details">
    <svg class="accent-band" viewBox="0 0 660 380" aria-hidden="true">
      <polygon class="band-white" points="0,228 58,166 250,166 660,276 660,292 250,182 64,182 0,250"/>
      <polygon class="band-orange" points="0,250 64,182 250,182 660,292 660,380 0,380"/>
    </svg>

    <div class="brand-name">Brightpath</div>

    <div class="holder">
      <p class="holder__name">Linda Marrowby</p>
      <p class="holder__role">Owner</p>
    </div>

    <ul class="contact-list">
      <li>
        <svg viewBox="0 0 16 16" aria-hidden="true"><path d="M3 1h3l1.5 4-2 1.3a9 9 0 0 0 4.2 4.2L11 8.5l4 1.5v3a2 2 0 0 1-2 2A13 13 0 0 1 1 3a2 2 0 0 1 2-2z"/></svg>
        <span>07862 413057</span>
      </li>
      <li>
        <svg viewBox="0 0 16 16" aria-hidden="true"><path d="M1 3h14v10H1z M2 4l6 5 6-5" stroke="#f6921e" stroke-width="1.2"/></svg>
        <span>lmarrowby@brightpath.co.uk</span>
      </li>
      <li>
        <svg viewBox="0 0 16 16" aria-hidden="true"><circle cx="8" cy="8" r="7"/><path d="M1 8h14M8 1c-3 3.5-3 10.5 0 14M8 1c3 3.5 3 10.5 0 14" stroke="#f6921e" stroke-width="1" fill="none"/></svg>
        <span>www.brightpath.co.uk</span>
      </li>
    </ul>
  </section>

  <section class="card card--front" aria-label="Card front">
    <div class="brand-name">Brightpath</div>
    <p class="website">www.brightpath.co.uk.</p>
  </section>

</main>
</body>
</html>
```